Logo for Internal Medicine practice

I want a logo for my Internal Medicine practice, I would like it to be with my name on it which is Lorena Benítez Prado.

I would like the business card to say the following (it is in Spanish since my practice is in Spanish):

Lorena Benítez Prado
Medicina Interna
Cel. 5587316420
lorenabenitezprado@correovela.com

Logo Text

Lorena Benítez

```html
<!DOCTYPE html>
<html lang="es">
<head>
<meta charset="utf-8">
<title>Lorena Benítez · Medicina Interna · Tarjeta de presentación</title>
<link rel="stylesheet" href="https://fonts.googleapis.com/css2?family=Mulish:wght@500;700;800&display=swap">
<style>
  :root {
    --navy: #0b3556;
    --red: #c90e22;
    --paper: #ffffff;
    --backdrop: #efedeb;
    --shadow: rgba(40, 30, 20, 0.16);
  }
  * { margin: 0; padding: 0; box-sizing: border-box; }
  html, body {
    width: 1200px;
    height: 750px;
    overflow: hidden;
    background: var(--backdrop);
    font-family: "Mulish", sans-serif;
  }
  .sheet {
    position: relative;
    width: 1200px;
    height: 750px;
  }
  .card {
    position: absolute;
    width: 520px;
    height: 300px;
    background: var(--paper);
    box-shadow: 0 18px 40px var(--shadow);
    overflow: hidden;
  }

  /* Front: identity */
  .card--front { left: 620px; top: 80px; }
  .identity {
    position: absolute;
    left: 70px;
    top: 100px;
    display: flex;
    align-items: center;
    gap: 22px;
  }
  .identity__dot {
    width: 62px;
    height: 62px;
    border-radius: 50%;
    background: var(--red);
    flex: none;
  }
  .identity__name {
    font-weight: 800;
    font-size: 32px;
    line-height: 1.1;
    color: var(--navy);
  }
  .identity__specialty {
    margin-top: 4px;
    font-weight: 700;
    font-size: 24px;
    color: var(--red);
  }

  /* Back: contact */
  .card--back { left: 60px; top: 380px; }
  .back__band {
    position: absolute;
    left: 0;
    top: 0;
    width: 150px;
    height: 100%;
    background: var(--red);
  }
  .back__bar {
    position: absolute;
    left: 100px;
    top: 40px;
    width: 46px;
    height: 190px;
    background: var(--navy);
    outline: 5px solid var(--paper);
  }
  .contact {
    position: absolute;
    left: 180px;
    top: 108px;
    list-style: none;
  }
  .contact__item {
    display: flex;
    align-items: center;
    gap: 12px;
    margin-bottom: 16px;
    font-weight: 700;
    font-size: 17px;
    color: var(--navy);
  }
  .contact__icon {
    width: 24px;
    height: 24px;
    flex: none;
  }
</style>
</head>
<body>
<main class="sheet">

  <section class="card card--front" aria-label="Anverso de la tarjeta">
    <div class="identity">
      <span class="identity__dot" aria-hidden="true"></span>
      <div>
        <p class="identity__name">Lorena Benítez</p>
        <p class="identity__specialty">Medicina Interna</p>
      </div>
    </div>
  </section>

  <section class="card card--back" aria-label="Reverso de la tarjeta">
    <div class="back__band"></div>
    <div class="back__bar"></div>
    <ul class="contact">
      <li class="contact__item">
        <svg class="contact__icon" viewBox="0 0 24 24" aria-hidden="true">
          <circle cx="12" cy="12" r="12" fill="var(--navy)"/>
          <rect x="6" y="8" width="12" height="8.5" rx="1" fill="none" stroke="#fff" stroke-width="1.4"/>
          <path d="M6.5 8.6 L12 13 L17.5 8.6" fill="none" stroke="#fff" stroke-width="1.4"/>
        </svg>
        <span>lorenabenitezprado@correovela.com</span>
      </li>
      <li class="contact__item">
        <svg class="contact__icon" viewBox="0 0 24 24" aria-hidden="true">
          <circle cx="12" cy="12" r="12" fill="var(--navy)"/>
          <path d="M9 6.5c.5 0 .9.3 1 .8l.6 2c.1.4 0 .8-.3 1.1l-.9.8c.6 1.3 1.6 2.4 2.9 3l.8-.9c.3-.3.7-.4 1.1-.3l2 .6c.5.1.8.5.8 1v1.4c0 .6-.5 1.1-1.1 1.1C10.9 17.1 6.9 13.1 6.9 8.2c0-.6.5-1.1 1.1-1.1z" fill="#fff"/>
        </svg>
        <span>5587316420</span>
      </li>
    </ul>
  </section>

</main>
</body>
</html>
```